Open Horizon Circle - invitation / brochure

​​I am in need of a bi-fold invitation/brochure for an educational series called "Open Horizon Circle". This dinner series provides education and community for "Women in Transition" these are women who are currently getting divorced, recently divorced, or widowed.

I am a partner of a wealth management boutique that advises a small number of high-net-worth families. Additionally, I am married to one of the most prominent family law attorneys in the country. The combination of these two unique perspectives has allowed me to see there is an unfortunate dearth of impactful, powerful, and useful resources to help wealthy women transition from being married to being single. (via divorce and/or death of their spouse)

What, How & WHY I do my job:
As a wealth manager, the "what" and "how" aspects of my job are not materially different from most of my competitors. However, the thing that makes me completely unique, and without competition, is "why" I do my job.

I do this because so many women experience unwelcome and unproductive feelings when the dilution of their marriage is complete AND because there is virtually no good place for them to obtain the important information they truly need to move forward and lead a happy, full, prosperous, productive, and fun life. In the absence of this information, many women experience unwelcome, unpleasant, and unproductive emotions.

For example, some experience shame or fear that they have failed. Others struggle with the belief they wasted a significant portion of their life. Some struggle with unresolved anger over the entire experience. It's very difficult to process and work through these emotions by yourself and it can be hard to get the support and guidance they need from their best friends (most are not trained in this area) may well be married (functional or otherwise) and they often times don't have the times to be there when the newly divorced or widowed women need them most.

Usually, these negative feelings are most intense when they are looking backward in time. However, I have seen women go on and lead remarkably impressive lives. Lives that are ​more ​full, richer, more fun, dynamic, and rewarding than they expected possible.

More about the WHY I do what I do - I created Open Horizon Circle so women in transition have a safe, supportive and comfortable space for these women to support each other. While each woman's story is unique, the emotional consequences are fairly common and they do not need to feel alone as they process the sometimes difficult, conflicting, and unpredictable emotions.

I want them to connect with each other because they have a great appreciation and empathy for what all the other women are experiencing. A bi-product of attending and participating in the dinner is to forge friendships and connections with the other woman in attendance so they can be resources to each other when they need help dealing with their own fear, anxiety, or anger. IMPORTANT NOTE - THIS IS NOT A THERAPY OR SUPPORT GROUP. Instead, this is a select group of very successful and accomplished women who have a shared experience and while each is navigating their own path, they have an opportunity to learn important information, in a safe place, where they can share their experience, strength, and hope with each other.

I want the invitation/brochure to feel very bespoke, thoughtfully curated, and specifically designed to address the most important and impactful areas of life, health, and wellness. I want the invitation/brochure to communicate that the presenters are the best in class and thought leaders in their respective areas of expertise. I also want to communicate that they have so much to be excited about. Because they have substantial financial resources, they have a unique opportunity to reinvent themselves and lead a life beyond their wildest dreams. I hope they can see how and why they can stop feeling the negative feelings of anger, sadness, fear, guilt, remorse, and regret. My goal is to get them to look forward (as opposed to backward where the negative emotions come from) so they can be optimistic, excited, happy, joyful, and enthusiastic because they get to be whoever they want; live wherever and however they want. They are not defined nor controlled by their past. They have full control and abundant resources at their disposal to be happier and more fulfilled than they ever hoped or imagined.

The feelings of optimism, excitement, energetic, and joyfulness are very important to the messaging of the Open Horizon Circle. I'd like this to be a consistent theme throughout the invitation/brochure. Basically moving from a dark, sad, and negative past to a bright, fun, optimistic, rewarding, fulfilling, and dynamic future.

To create an exciting, rewarding and vibrant life they will want to (in some cases need to) learn new information and skills from the leading authorities in the most important and impactful areas of life.

The presenters at each dinner will focus on one of the "8 Dimensions of Wellness" so they can make thoughtful and informed decisions without fear, anxiety, and stress.

If you think of marriage as two people sailing a ship or flying a plane, the husband and wife often divide the responsibilities of running their affairs because it's too much for one person to manage all by themselves; besides they have a spouse who can help and often times they have different expertise. For illustration purposes, let's say the husband manages the even-numbered items and the wife manages the odd number of items. Each manages half but together everything is well managed and nothing falls through the cracks.

Post-divorce, the husband and wife now each have their own boat to sail and are responsible for all the items (odd and even-numbered) of their ship.

Unfortunately, these women are having to manage items that she has little to no experience with the even-numbered items the husband used to manage during the marriage. They have to take sole control of complicated matters that have serious and long-lasting consequences. That's great if they do a good job. However, given the scope, scale, and complexity of 7-10 figure net worth chances are they won't have the experience, expertise, intellectual resources, and time to manage all the even and odd numbers optimally.

The format of the Open Horizon Circle events will be an intimate dinner conversation, in a private room, at a 5 star restaurant in Chicago. There will be a thoughtfully curated group of 4-10 women at one round table to facilitate an interesting and informative presentation. It will be specifically curated for them and delivered. There is no cost to attend the event and they are welcome to attend as many as they like. I will be covering all the expenses related to dinner, drinks, valet parking, and the speaker or presenter.

Each monthly dinner will focus on 1 of the 8 Dimensions of Wellness:

1. Physical - Physical Activity, Good Nutrition, Sleep, Preventing Illness & Injury, and Managing Chronic Health Conditions.

2. Emotional - Coping Effectively with life and creating satisfying relationships.

3. Social - Developing a sense of connection, belonging, and a well-developed support system.

4. Intellectual - Recognizing one’s creative abilities and finding ways to expand knowledge and skills. Boost cognitive function, stimulate the brain, and fuel learning.

5. Environmental - Occupying pleasant, stimulating environments that support well-being.

6. Spiritual - Expanding a sense of purpose and meaning in life, including one’s morals and ethics. (May or may not involve religious activities). Meditation

7. Vocational - Gaining personal satisfaction and enrichment from one's work (maybe academic or professional). Share your talents, wisdom, and experience.

8. Financial - Satisfaction with current and future financial situations.

I'd like the invitation/brochure to give a general overview of the 8 dimensions of wellness and that each gathering will focus on one of the eight. The presentation will be done by women (some of whom went through a divorce or the death of a spouse) who are widely recognized as experts in their respective fields. The female presenters will be highly qualified and credentialed in their field - this could mean they are MDs or PhDs and/or have decades of experience in their specific area of expertise.

I'd like the invitation to be "timeless" meaning that it doesn't have specific dates, times, or locations included. However, if someone would like more information and details they can call or email me for the specific details of the next couple of dates, topics, locations, and menus. I am also open to having a QR code available on the brochure for them to contact me for additional information. Once they contact my office they will receive I will receive all the detailed information via a PDF so they can RSVP if they would like to attend. My goal is that I don't want the invitation/brochure to expire even though the event details change every month.

I will market the Open Horizon Circle program by distributing the invitation/brochures available via therapists, divorce lawyers, and grief counselors that specialize in this demographic of women in transition. They in turn will share the invitation/brochure with their woman in transition clients if they think they would benefit from the program

The look and feel I am going for with the brochure/invitation is high-end, contemporary, carefully curated content for a very special and specific community of high-net-worth women in transition that has the resources to be and do anything they want.

Vellora
Marlowe Crest
Duvaine
Kestrel Onyx Card
Shopping in Paris and London
Flying private
Vacationing in the Riviera & Monaco.
Beautiful people
Multi-generational - kids and grandkids.

The theme, feel, and messaging of the invitation/brochure should be consistent with the concept of moving away from – sadness, fear, regret, failure, and negative. And moving towards – joyful, happy, optimistic, exciting, successful, energetic, and contentment.

This information is intended to be informative, empowering, uplifting, transformational, and helpful - so they can lead a life that is bigger, brighter, and better than they ever dreamed of experiencing.

Target Market(s)

Wealthy woman who are currently getting divorced, recently divorced, or widowed. Generally the women will be mid-fourties and older..

Industry/Entity Type

Financial Services targeting wealthy windows and divorced woman.

Font styles to use
Serif
Sans Serif

Requirements
Must have
• The look and feel I am going for with the brochure/invitation is high-end, contemporary, carefully curated content for a very special and specific community of high-net-worth women in transition that has the resources to be and do anything they want. PLEASE ENSURE 70% OF THE WOMAN IN THE INVITATAION/BROCHURE OF NON-WHITE RACES & ETHNICITIES. The theme, feel, and messaging of the invitation/brochure should be consistent with the concept of moving away from – sadness, fear, regret, failure, and negative. And moving towards – joyful, happy, optimistic, exciting, successful, energetic, and contentment. This information is intended to be informative, empowering, uplifting, transformational, and helpful - so they can lead a life that is bigger, brighter, and better than they ever dreamed of experiencing.

```html
<!DOCTYPE html>
<html lang="en">
<head>
<meta charset="utf-8">
<title>Open Horizon Circle — Bi-fold Invitation</title>
<link href="https://fonts.googleapis.com/css2?family=Cormorant+Garamond:wght@400&family=Oswald:wght@300;400&family=Source+Sans+3:wght@400&family=Mrs+Saint+Delafield&display=swap" rel="stylesheet">
<style>
  :root {
    --backdrop: #cccccc;
    --navy: #0c0c27;
    --gold: #e0a93a;
    --gold-soft: #c9943a;
    --gold-light: #f6e27a;
    --gold-deep: #c48a1c;
    --wave-tone: rgba(90, 90, 112, 0.16);
  }
  * { margin: 0; padding: 0; box-sizing: border-box; }
  html, body { width: 1200px; height: 1200px; overflow: hidden; background: var(--backdrop); }
  .canvas { position: relative; width: 1200px; height: 1200px; }
  .panel {
    position: absolute;
    background: var(--navy);
    overflow: hidden;
    box-shadow: 2px 3px 6px rgba(0,0,0,0.35);
  }
  .panel--cover { left: 348px; top: 84px; width: 504px; height: 326px; }
  .panel--inside { left: 97px; top: 443px; width: 1005px; height: 325px; }
  .panel--back { left: 348px; top: 794px; width: 504px; height: 327px; }

  .silk-band {
    position: absolute;
    background: linear-gradient(160deg, var(--gold-deep) 0%, var(--gold-light) 22%, var(--gold-deep) 45%, #f2d45a 62%, var(--gold-light) 80%, var(--gold-deep) 100%);
  }
  .wave-area {
    position: absolute;
    background: linear-gradient(155deg, transparent 0%, var(--wave-tone) 45%, var(--wave-tone) 55%, transparent 100%);
  }
  .wave-area--cover { left: 0; top: 0; width: 410px; height: 160px; }
  .wave-area--back { left: 80px; top: 89px; width: 424px; height: 215px; }

  .cover-title {
    position: absolute; left: 140px; top: 160px;
    font-family: "Mrs Saint Delafield", cursive; font-weight: 400;
    font-size: 58px; line-height: 1;
    color: var(--gold); white-space: nowrap;
    background: linear-gradient(90deg, #e8b640, #f5d67a 50%, #d9a33a);
    -webkit-background-clip: text; background-clip: text; -webkit-text-fill-color: transparent;
  }

  .wellness-number {
    position: absolute; left: 34px; top: 15px; width: 160px; text-align: center;
    font-family: "Cormorant Garamond", serif; font-size: 220px; line-height: 1;
    background: linear-gradient(180deg, var(--gold-light), var(--gold-deep) 55%, var(--gold-light));
    -webkit-background-clip: text; background-clip: text; -webkit-text-fill-color: transparent;
  }
  .wellness-caption {
    position: absolute; left: 34px; top: 205px; width: 160px; text-align: center;
    font-family: "Source Sans 3", sans-serif; font-size: 20px; line-height: 23px;
    color: var(--gold-light); letter-spacing: 0.5px;
  }
  .rule { position: absolute; width: 1px; background: var(--gold); }
  .rule--main { left: 227px; top: 44px; height: 236px; width: 2px; }
  .rule--outer-left { left: 222px; top: 58px; height: 201px; }
  .rule--outer-right { left: 233px; top: 58px; height: 201px; }

  .dimension { position: absolute; width: 196px; }
  .dimension--mid { width: 148px; }
  .dimension--right { width: 180px; }
  .dimension__name {
    font-family: "Oswald", sans-serif; font-weight: 300;
    font-size: 14px; letter-spacing: 1.6px; color: var(--gold);
    line-height: 18px; margin-bottom: 7px;
  }
  .dimension__text {
    font-family: "Source Sans 3", sans-serif; font-size: 8.4px; line-height: 12.4px;
    color: var(--gold-soft);
  }

  .back-frame {
    position: absolute; left: 297px; top: 89px; width: 59px; height: 59px;
    border: 1px solid var(--gold-soft);
  }
  .contact {
    position: absolute; left: 0; top: 254px; width: 297px;
    font-family: "Source Sans 3", sans-serif; color: var(--gold);
  }
  .contact__label {
    font-family: "Oswald", sans-serif; font-weight: 300; font-size: 8px;
    letter-spacing: 1.3px; text-align: right; margin-bottom: 12px;
  }
  .contact__line { font-size: 8.4px; line-height: 12.4px; text-align: right; }
  .contact__line span { margin-right: 6px; }
</style>
</head>
<body>
<main class="canvas">

  <section class="panel panel--cover">
    <div class="wave-area wave-area--cover" role="img" aria-label="Fine flowing wave-line ornament"></div>
    <h1 class="cover-title">Open Horizon Circle</h1>
    <div class="silk-band" style="left:0;top:237px;width:297px;height:89px;" role="img" aria-label="Flowing gold silk fabric"></div>
  </section>

  <section class="panel panel--inside">
    <div class="wellness-number">8</div>
    <p class="wellness-caption">DIMENSIONS<br>OF WELLNESS</p>
    <span class="rule rule--outer-left"></span>
    <span class="rule rule--main"></span>
    <span class="rule rule--outer-right"></span>

    <article class="dimension" style="left:266px;top:57px;">
      <h2 class="dimension__name">PHYSICAL</h2>
      <p class="dimension__text">Physical Activity, Good Nutrition, Sleep, Preventing Illness &amp; Injury, and Managing Chronic Health Conditions.</p>
    </article>
    <article class="dimension" style="left:266px;top:146px;">
      <h2 class="dimension__name">EMOTIONAL</h2>
      <p class="dimension__text">Coping Effectively with life and creating satisfying relationships.</p>
    </article>
    <article class="dimension" style="left:266px;top:221px;">
      <h2 class="dimension__name">SOCIAL</h2>
      <p class="dimension__text">Developing a sense of connection, belonging, and a well-developed support system.</p>
    </article>

    <article class="dimension dimension--mid" style="left:546px;top:42px;">
      <h2 class="dimension__name">INTELLECTUAL</h2>
      <p class="dimension__text">Recognizing one’s creative abilities and finding ways to expand knowledge and skills. Boost cognitive function, stimulate the brain, and fuel learning.</p>
    </article>
    <div class="silk-band" style="left:503px;top:147px;width:236px;height:47px;" role="img" aria-label="Flowing gold silk fabric"></div>
    <article class="dimension dimension--mid" style="left:546px;top:237px;">
      <h2 class="dimension__name">ENVIRONMENTAL</h2>
      <p class="dimension__text">Occupying pleasant, stimulating environments that support well-being.</p>
    </article>

    <article class="dimension dimension--right" style="left:768px;top:42px;">
      <h2 class="dimension__name">SPIRITUAL</h2>
      <p class="dimension__text">Expanding a sense of purpose and meaning in life, including one’s morals and ethics. (May or may not involve religious activities), Meditation.</p>
    </article>
    <article class="dimension dimension--right" style="left:768px;top:141px;">
      <h2 class="dimension__name">VOCATIONAL</h2>
      <p class="dimension__text">Gaining personal satisfaction and enrichment from one’s work (maybe academic or professional). Share your talents, wisdom, and experience.</p>
    </article>
    <article class="dimension dimension--right" style="left:768px;top:237px;">
      <h2 class="dimension__name">FINANCIAL</h2>
      <p class="dimension__text">Satisfaction with current and future financial situations.</p>
    </article>
  </section>

  <section class="panel panel--back">
    <div class="wave-area wave-area--back" role="img" aria-label="Fine flowing wave-line ornament"></div>
    <div class="silk-band" style="left:0;top:0;width:297px;height:89px;" role="img" aria-label="Flowing gold silk fabric"></div>
    <div class="back-frame"></div>
    <div class="contact">
      <p class="contact__label">FOR MORE INFORMATION</p>
      <p class="contact__line"><span>P.</span>123-456-7890</p>
      <p class="contact__line"><span>E.</span>hello@openhorizoncircle.com</p>
    </div>
  </section>

</main>
</body>
</html>
```